Career Ad - Graphic Image to Attract New Team Members to our Company

We would like a career ad to be used for recruiting staff. This ad will be posted through our social media sites and may also be printed on post cards. Concept we like so far (however we are open to other creative ideas) is a photo in the background with printing on top. The color would be our brand color : blue. As for content, words like "We're Hiring" or "Come join our team" we'd also like to have reference to our website https://lindenvale.ca/about/careers and our email careers@lindenvale.ca Of course, our logo and company name, which is attached in the files
Target Market(s)
Professional
Requirements
Must have
- company logo
Nice to have
- visually apealling

```html
<!DOCTYPE html>
<html lang="en">
<head>
<meta charset="utf-8">
<title>Lindenvale Brokers — We're Hiring</title>
<link rel="stylesheet" href="https://fonts.googleapis.com/css2?family=Archivo+Black&family=Cinzel:wght@700&family=Roboto:wght@700&display=swap">
<style>
  :root {
    --brand-blue: #2b4fa6;
    --brand-blue-deep: #1f3f8f;
    --navy: #1d2856;
    --white: #ffffff;
    --wood-dark: #3a2a20;
    --wood-mid: #6b4e3a;
    --paper: #d9d4cc;
  }
  * { margin: 0; padding: 0; box-sizing: border-box; }
  html, body {
    width: 1200px;
    height: 1200px;
    overflow: hidden;
    background: var(--white);
  }
  .career-ad {
    position: relative;
    width: 1200px;
    height: 1200px;
    overflow: hidden;
  }
  .background-photo {
    position: absolute;
    inset: 0;
    background:
      radial-gradient(ellipse 420px 300px at 560px 560px, rgba(210,170,140,0.55), transparent 70%),
      radial-gradient(ellipse 300px 420px at 170px 760px, rgba(225,222,215,0.75), transparent 70%),
      radial-gradient(ellipse 260px 220px at 1020px 260px, rgba(200,205,212,0.55), transparent 70%),
      linear-gradient(160deg, var(--wood-mid) 0%, var(--wood-dark) 55%, #2b1f18 100%);
  }
  .header-shape {
    position: absolute;
    top: 0;
    left: 0;
    width: 1200px;
    height: 460px;
  }
  .brand {
    position: absolute;
    top: 62px;
    left: 0;
    width: 1200px;
    display: flex;
    flex-direction: column;
    align-items: center;
    color: var(--navy);
    font-family: "Cinzel", serif;
    font-weight: 700;
  }
  .brand-mark {
    width: 78px;
    height: 78px;
    background: var(--navy);
    margin-bottom: 14px;
  }
  .brand-name {
    font-size: 54px;
    line-height: 1;
    letter-spacing: 1px;
  }
  .brand-tagline {
    font-size: 30px;
    line-height: 1;
    letter-spacing: 5px;
    margin-top: 12px;
  }
  .headline {
    position: absolute;
    left: 0;
    top: 690px;
    width: 1200px;
    text-align: center;
    font-family: "Archivo Black", sans-serif;
    font-size: 190px;
    line-height: 0.92;
    color: var(--white);
    letter-spacing: 2px;
    text-shadow:
      6px 6px 0 var(--brand-blue-deep),
      -3px 3px 0 var(--brand-blue-deep),
      3px -3px 0 var(--brand-blue-deep),
      -3px -3px 0 var(--brand-blue-deep),
      10px 10px 0 var(--white);
  }
  .contact-bar {
    position: absolute;
    left: 0;
    bottom: 0;
    width: 1200px;
    height: 137px;
    background: var(--brand-blue);
    display: flex;
    align-items: center;
    justify-content: space-between;
    padding: 0 80px;
    font-family: "Roboto", sans-serif;
    font-weight: 700;
    font-size: 38px;
    color: var(--white);
  }
</style>
</head>
<body>
  <main class="career-ad">
    <div class="background-photo" role="img" aria-label="Photo of two professionals shaking hands across a wooden desk with clipboards, documents and a laptop"></div>

    <svg class="header-shape" viewBox="0 0 1200 460" aria-hidden="true">
      <path d="M140 0 L1060 0 C1060 190 860 340 600 440 C340 340 140 190 140 0 Z" fill="var(--brand-blue)"/>
      <path d="M190 0 L1010 0 C1010 165 825 305 600 398 C375 305 190 165 190 0 Z" fill="var(--white)"/>
    </svg>

    <header class="brand">
      <div class="brand-mark"></div>
      <div class="brand-name">LINDENVALE</div>
      <div class="brand-tagline">BROKERS</div>
    </header>

    <h1 class="headline">WE’RE<br>HIRING</h1>

    <footer class="contact-bar">
      <span class="contact-web">www.lindenvale.ca</span>
      <span class="contact-email">careers@lindenvale.ca</span>
    </footer>
  </main>
</body>
</html>
```